Disability Service Provider Website

We are working with VEP, which provides services and job training designed to educate, facilitate, train, and assist individuals with disabilities. They describe their clients using words like Unity and Unique.
Some sites to use for content/competitors and inspiration:
https://www.skillmora.com
https://www.pwkd.org
https://www.bellowhaven.org
https://www.openmeadow.org
https://corvelan.org
Thank you for taking the time to consider designing a website for us. We are web developers based in Stockton, CA, USA. Most of our projects go through the same process. Understanding this process may help you win a project with us. We custom-code all of our websites in-house. We don’t have any requirements as to what tools you use for your design, but we prefer Figma files. For any design that we label as four-stars, we send it to the client for review. The client picks the final design they want us to use. Once we complete this process, we will continue to show additional clients all the four-star sites and purchase them later. Your designs will have multiple chances to sell. For better chances of success, we ask that you follow these guidelines.
IMAGES:
If you use any images or icons in the design, we ask that you have a link to the asset so we can purchase the image/icon. Most of the designs we submit do not have the customer’s images on them unless they have some great images. Be creative; show us the feeling you are trying to portray with your image choices. Use any royalty-free site you choose. We subscribe to Stellic and mainly use their images, but we can purchase images outside of Stellic.
PLEASE NOTE: we will not submit designs to clients with watermarks on the images.
FONTS:
We ask that you identify the fonts used in the design. This can be done in a message if you want. We typically use Bramble Fonts and Stellic Fonts.
CONTENT:
We're always open to different content and ideas. We often submit designs with stock images so the client can see our vision. We typically take pictures after the website launch to use their images with our vision. Lorem Ipsum is fine for paragraphs, but we ask that you write the headers in correct English. We want to be able to show the vision and identify the sections of the website.
INSPIRATION:
We typically add a couple of links in the brief of websites we like to help you get started in your design.
REVISIONS:
We do not often ask for revisions of the designs unless we see something in the design that may not appeal to the client. If there are slight changes that we want to make, we do that in the development process.
FEEDBACK:
We rarely give feedback on designs during the design process. We are working on many website projects and do not have the time to provide feedback. We usually respond if your request is well thought out and asks specific questions, but a note asking “feedback, please” usually goes unanswered.
Number of Pages Required
1 page
Look and feel
Each slider illustrates characteristics of the customer's brand and the style your logo design should communicate.

```html
<!DOCTYPE html>
<html lang="en">
<head>
<meta charset="utf-8">
<title>VEP – Uniting Hearts, Celebrating Uniqueness</title>
<link href="https://fonts.googleapis.com/css2?family=Noto+Sans:wght@400;500;600;700&display=swap" rel="stylesheet">
<style>
:root{
  --red:#9b0d14;
  --navy:#0f1f5c;
  --ink:#1d2a4d;
  --slate:#5b6b82;
  --text:#7a7f8c;
  --sky:#eaf5fa;
  --bar:#3b4a7c;
  --deep:#1b3550;
  --orange:#e8892b;
  --white:#fff;
}
*{box-sizing:border-box;margin:0;padding:0}
html,body{width:1200px;height:4320px;overflow:hidden}
body{font-family:"Noto Sans",sans-serif;color:var(--ink);background:var(--white);position:relative}
.abs{position:absolute}
.photo{position:absolute}

/* header */
.topbar{left:0;top:0;width:1200px;height:34px}
.top-info{top:9px;font-size:10px;color:#fff;display:flex;align-items:center;gap:6px}
.quote-btn{left:845px;top:8px;width:110px;height:18px;background:#2f6f78;color:#fff;font-size:10px;text-align:center;line-height:18px;border-bottom:2px solid #5fb3bf}
.logo{left:134px;top:22px;font-size:42px;font-weight:700;color:var(--red);letter-spacing:1px;line-height:1}
.nav{left:403px;top:50px;display:flex;gap:0;font-size:11px;color:var(--slate)}
.nav a{text-decoration:none;color:inherit;margin-right:36px}
.nav a.active{color:#1f4fa3;font-weight:600}

/* hero */
.hero-photo{left:0;top:80px;width:1200px;height:760px;background:linear-gradient(90deg,#050708 0%,#1a2225 35%,#3d4a4c 60%,#6e7471 80%,#8b8a82 100%)}
.hero-title{left:128px;top:262px;font-size:41px;line-height:48px;font-weight:600;color:#fff}
.hero-text{left:129px;top:386px;width:460px;font-size:19px;line-height:28px;color:#fff}
.btn-red{background:var(--red);color:#fff;font-weight:700;text-align:center}
.hero-btn{left:129px;top:503px;width:155px;height:39px;border-radius:20px;font-size:12px;line-height:39px}

/* who we are */
.sky{left:0;width:1200px;background:var(--sky)}
.eyebrow{font-size:12px;color:var(--red);font-weight:500;border-bottom:2px solid var(--red);padding-bottom:3px}
.h-center{width:1200px;text-align:center;left:0}
.section-title{font-size:41px;font-weight:600;color:var(--navy)}
.lead{font-size:13.5px;line-height:22px;color:var(--text)}
.card{width:276px;height:243px;top:1085px;background:#fff;border-bottom:4px solid var(--red);box-shadow:0 4px 14px rgba(30,60,90,.10);text-align:center}
.card h3{position:absolute;left:0;width:100%;font-size:21px;font-weight:600;color:#59657c;letter-spacing:.5px}
.card p{position:absolute;left:38px;width:200px;font-size:13px;line-height:22px;color:var(--text)}

/* challenges */
.h2{font-size:37px;line-height:47px;font-weight:600;color:var(--navy)}
.sub{font-size:19px;font-weight:500;color:var(--navy)}
.body-s{font-size:12px;line-height:19.5px;color:var(--text)}
.btn-sq{left:133px;top:1855px;width:137px;height:38px;font-size:14px;line-height:38px;font-weight:600;display:flex;align-items:center;justify-content:center;gap:10px}

/* service strip */
.bar{background:var(--bar);width:60px;height:453px;top:2060px}
.vtext{position:absolute;left:8px;bottom:48px;transform-origin:left bottom;transform:rotate(-90deg) translateY(34px);white-space:nowrap;color:#fff;font-size:12px;line-height:16px;width:300px}
.vtext b{display:block;font-size:15px;font-weight:700}

/* testimonials */
.quote-text{font-size:17px;line-height:31px;color:var(--ink)}

/* contact */
.form-card{left:588px;top:3220px;width:487px;height:556px;background:#fff;border-top:3px solid var(--red);border-radius:6px;box-shadow:0 4px 18px rgba(20,40,80,.10)}
.label{font-size:14px;font-weight:600;color:#1f4f87}
.field{border:1px solid #b8bfc9;border-radius:2px;background:#fff;font-size:11px;color:#8c929c;padding:0 16px;line-height:44px}
.c-icon{width:36px;height:36px;border-radius:50%;background:#fff;box-shadow:0 2px 8px rgba(30,60,120,.14)}
.c-text{font-size:13px;color:#6a7282}

/* footer */
.f-head{font-size:15px;font-weight:600;color:#fff}
.f-text{font-size:11.5px;line-height:21px;color:#fff}
.social{width:34px;height:34px;border:1px solid #fff}
</style>
</head>
<body>

<!-- header -->
<svg class="abs topbar" viewBox="0 0 1200 34" aria-hidden="true"><path d="M0 0H1200V34H470C430 34 420 0 380 0Z" fill="#1d2330"/><path d="M0 0H380C420 0 430 34 470 34H0Z" fill="#fff"/></svg>
<div class="abs" style="left:0;top:34px;width:1200px;height:46px;background:#fff;border-bottom:1px solid #e3e6ea"></div>
<div class="abs top-info" style="left:465px"><svg width="8" height="10" viewBox="0 0 8 10"><path d="M4 0a4 4 0 0 1 4 4c0 3-4 6-4 6S0 7 0 4a4 4 0 0 1 4-4z" fill="#fff"/><circle cx="4" cy="4" r="1.4" fill="#1d2330"/></svg>48 Larkfield Rd., Stockton, CA 95201</div>
<div class="abs top-info" style="left:705px">Follow Us: <span style="display:inline-block;width:6px;height:6px;border-radius:50%;background:#fff"></span><span style="display:inline-block;width:6px;height:6px;border-radius:50%;background:#fff"></span><span style="display:inline-block;width:6px;height:6px;border-radius:50%;background:#fff"></span></div>
<div class="abs quote-btn">GET QUOTATION</div>
<div class="abs logo">VEP</div>
<nav class="abs nav"><a class="active">Home</a><a>Services</a><a>About Us</a><a>Our Team</a><a>And more</a><a>Contact Us</a></nav>

<!-- hero -->
<div class="photo hero-photo" role="img" aria-label="Photo: two colleagues smiling at a laptop in a modern office, one seated in a wheelchair"></div>
<div class="abs hero-title">Uniting Hearts,<br>Celebrating Uniqueness</div>
<p class="abs hero-text">Lorem ipsum dolor sit amet, consectetur adipi scing elit, sed do eiusmod tempor incidid unt ut labore et dolore magna aliqua.</p>
<div class="abs btn-red hero-btn">READ MORE</div>
<svg class="abs" style="left:0;top:620px" width="1200" height="220" viewBox="0 0 1200 220" aria-hidden="true">
  <path d="M0 165C300 150 600 120 820 110C980 90 1100 50 1200 5V220H0Z" fill="#eaf5fa"/>
  <path d="M0 165C260 160 560 140 820 110C600 150 300 190 0 212Z" fill="#9b0d14"/>
</svg>

<!-- who we are -->
<div class="abs sky" style="top:840px;height:563px"></div>
<div class="abs h-center" style="top:870px"><span class="eyebrow">WHO WE ARE</span></div>
<h1 class="abs h-center section-title" style="top:904px">Embracing Uniqueness, Building Unity</h1>
<p class="abs lead" style="left:175px;top:976px;width:800px;text-align:center">Lorem ipsum dolor sit amet, consectetur adipiscing elit, sed do eiusmod tempor incididunt ut labore et dolore magna aliqua . Ut enim ad minim veniam, quis laboris nisi ut aliquip ex ea commodo consequat. Lorem ipsum dolor sit am et, consectetur adipiscing elit, sed do eiusmod te a</p>

<div class="abs card" style="left:152px">
  <svg class="abs" style="left:110px;top:62px" width="56" height="60" viewBox="0 0 56 60" fill="none" stroke="#9b0d14" stroke-width="3" stroke-linejoin="round"><circle cx="24" cy="10" r="7"/><path d="M12 52V30l14-6 12 12"/><path d="M4 56h48l-8-10H22"/></svg>
  <h3 style="top:150px">CLIENT-CENTRIC</h3>
</div>
<div class="abs card" style="left:462px">
  <h3 style="top:42px">PROFESSIONAL</h3>
  <p style="top:88px">Lorem ipsum dolor sit amet, consectetur adipiscing elit, se d do eiusmod tempor incidid unt ut labore et dolore magna ali</p>
</div>
<div class="abs card" style="left:768px">
  <svg class="abs" style="left:104px;top:60px" width="68" height="66" viewBox="0 0 68 66" fill="none" stroke="#9b0d14" stroke-width="3"><path d="M34 7L61 27L51 58H17L7 27Z"/><g fill="#fff"><circle cx="34" cy="7" r="5"/><circle cx="61" cy="27" r="5"/><circle cx="51" cy="58" r="5"/><circle cx="17" cy="58" r="5"/><circle cx="7" cy="27" r="5"/></g></svg>
  <h3 style="top:150px">EXPERTISE</h3>
</div>

<!-- challenges -->
<div class="abs" style="left:133px;top:1530px"><span class="eyebrow" style="font-size:11px">WHO WE ARE</span></div>
<h2 class="abs h2" style="left:133px;top:1565px">Navigating Challenges,<br>Unlocking Opportunities</h2>
<div class="abs sub" style="left:133px;top:1681px">Empowerment through Opportunity and Inclusion</div>
<p class="abs body-s" style="left:133px;top:1723px;width:455px">Lorem ipsum dolor sit amet, consectetur adipiscing elit, sed do eiusmod temp or incididunt ut labore et dolore magna aliqua. Ut enim ad minim veniam, quis laboris nisi ut aliquip ex ea commodo consequat.</p>
<p class="abs body-s" style="left:133px;top:1792px;width:455px">Lorem ipsum dolor sit amet, consectetur adipiscing elit, sed do eiusmod temp or incididunt ut labore et dolore magna aliqua.</p>
<div class="abs btn-red btn-sq">Contact us <svg width="16" height="12" viewBox="0 0 16 12" fill="none" stroke="#fff" stroke-width="1.6"><path d="M1 6h13M9 1l5 5-5 5"/></svg></div>

<svg class="abs" style="left:640px;top:1490px" width="540" height="440" viewBox="0 0 540 440" aria-hidden="true">
  <circle cx="207" cy="223" r="218" fill="#f1f1df"/>
  <circle cx="57" cy="381" r="47" fill="#9b0d14"/>
</svg>
<div class="photo" role="img" aria-label="Photo: friends giving a high five at an outdoor table" style="left:644px;top:1496px;width:424px;height:424px;border-radius:50%;background:radial-gradient(circle at 45% 45%,#c9b59c 0%,#8f7a63 40%,#4a5a3e 100%)"></div>
<div class="photo" role="img" aria-label="Photo: three smiling friends posing together" style="left:952px;top:1538px;width:202px;height:202px;border-radius:50%;background:radial-gradient(circle at 50% 55%,#c08a5e 0%,#6b5a4a 45%,#2f2f30 100%)"></div>

<!-- services strip -->
<div class="photo" role="img" aria-label="Photo: smiling woman in a wheelchair holding a phone" style="left:0;top:2060px;width:340px;height:453px;background:linear-gradient(90deg,#b9b5b1,#d9d4cf 45%,#8e8680)"></div>
<div class="abs bar" style="left:340px"><div class="vtext"><b>Skills Training</b>Lorem ipsum dolor sit amet, consectetu</div><svg class="abs" style="left:14px;bottom:16px" width="14" height="24" viewBox="0 0 14 24" fill="none" stroke="#fff" stroke-width="1.6"><path d="M7 23V2M2 7l5-5 5 5"/></svg></div>
<div class="photo" role="img" aria-label="Photo: mother and son laughing together" style="left:400px;top:2060px;width:400px;height:453px;background:linear-gradient(180deg,#d8d1ca 0%,#8d7a6b 45%,#27304f 80%,#1e2746 100%)"></div>
<div class="abs" style="left:440px;top:2315px;width:52px;height:52px;border-radius:50%;background:#fff"></div>
<svg class="abs" style="left:452px;top:2326px" width="28" height="30" viewBox="0 0 56 60" fill="none" stroke="#3b4a7c" stroke-width="4"><circle cx="24" cy="10" r="7"/><path d="M12 52V30l14-6 12 12"/><path d="M4 56h48l-8-10H22"/></svg>
<div class="abs" style="left:439px;top:2386px;font-size:16px;font-weight:700;color:#fff">Wellness Programs</div>
<p class="abs" style="left:439px;top:2409px;width:330px;font-size:13px;line-height:20px;color:#fff">Lorem ipsum dolor sit amet, consectetur adipiscing elit, sed do eiusmod tempor incididunt ut labore et dolore magna aliqua. Ut enim ad minim</p>
<svg class="abs" style="left:439px;top:2480px" width="26" height="14" viewBox="0 0 26 14" fill="none" stroke="#fff" stroke-width="1.6"><path d="M1 7h23M18 1l6 6-6 6"/></svg>
<div class="photo" role="img" aria-label="Photo: woman in a pink blazer with a white cane outside a building" style="left:800px;top:2060px;width:340px;height:453px;background:linear-gradient(90deg,#dfe3e6,#c9a3ae 45%,#b93b78 60%,#9a9b98)"></div>
<div class="abs bar" style="left:1140px"><div class="vtext"><b>Job Placement</b>Lorem ipsum dolor sit amet, consectetu</div><svg class="abs" style="left:14px;bottom:16px" width="14" height="24" viewBox="0 0 14 24" fill="none" stroke="#fff" stroke-width="1.6"><path d="M7 23V2M2 7l5-5 5 5"/></svg></div>

<!-- testimonials -->
<div class="abs sky" style="top:2513px;height:645px"></div>
<div class="abs h-center" style="top:2577px;font-size:16px;color:var(--red);font-weight:500">TESTIMONIALS</div>
<h2 class="abs h-center" style="top:2604px;font-size:31px;font-weight:600;color:var(--navy)">What Our Clients are Saying</h2>
<svg class="abs" style="left:0;top:2700px" width="1200" height="240" viewBox="0 0 1200 240" aria-hidden="true">
  <path d="M198 195C300 100 420 50 604 45C790 50 910 100 1008 195" fill="none" stroke="#3f8fd2" stroke-width="2" stroke-dasharray="6 5"/>
  <g fill="#9b0d14"><path d="M580 148h16v16c0 10-6 16-14 18l-2-5c5-2 7-6 7-10h-7z"/><path d="M604 148h16v16c0 10-6 16-14 18l-2-5c5-2 7-6 7-10h-7z"/></g>
</svg>
<div class="photo" role="img" aria-label="Portrait photo of a client" style="left:544px;top:2685px;width:120px;height:120px;border-radius:50%;background:radial-gradient(circle,#c49a7b 0%,#7a6858 60%,#4f5b66 100%);border:3px solid #fff"></div>
<div class="photo" role="img" aria-label="Portrait photo of a client" style="left:346px;top:2740px;width:74px;height:74px;border-radius:50%;background:radial-gradient(circle,#d6b49a,#8b8a8c);border:3px solid #fff"></div>
<div class="photo" role="img" aria-label="Portrait photo of a client" style="left:787px;top:2740px;width:74px;height:74px;border-radius:50%;background:radial-gradient(circle,#e0c6a4,#3b3f4a);border:3px solid #fff"></div>
<div class="photo" role="img" aria-label="Portrait photo of a client" style="left:160px;top:2857px;width:76px;height:76px;border-radius:50%;background:radial-gradient(circle,#c69e83,#9a9794);border:3px solid #fff"></div>
<div class="photo" role="img" aria-label="Portrait photo of a client" style="left:970px;top:2857px;width:76px;height:76px;border-radius:50%;background:radial-gradient(circle,#d4b8a4,#8c8a86);border:3px solid #fff"></div>
<p class="abs quote-text" style="left:295px;top:2896px;width:615px;text-align:center">Lorem ipsum dolor sit amet, consectetur adipiscing elit, sed do eiusmod te dunt ut labore et dolore magna aliqua .dipiscing elit, sed do eiusmod temp dunt ut labore et dolore magna aliqua .dipiscing elit, sed</p>
<div class="abs h-center" style="top:3010px;font-size:17px;color:var(--orange);letter-spacing:2px">★★★★★</div>
<div class="abs h-center" style="top:3037px;font-size:17px;font-weight:600;color:var(--orange)">Maren Tollis</div>
<div class="abs h-center" style="top:3068px;font-size:10px;color:var(--ink)">Client</div>
<svg class="abs" style="left:464px;top:3024px" width="48" height="48" viewBox="0 0 48 48"><circle cx="24" cy="24" r="22" fill="#1c3a2e"/><path d="M32 24H16M22 17l-7 7 7 7" fill="none" stroke="#fff" stroke-width="2"/></svg>
<svg class="abs" style="left:694px;top:3024px" width="48" height="48" viewBox="0 0 48 48"><circle cx="24" cy="24" r="22" fill="#9b0d14"/><path d="M16 24h16M26 17l7 7-7 7" fill="none" stroke="#fff" stroke-width="2"/></svg>

<!-- contact -->
<div class="abs" style="left:140px;top:3280px;font-size:33px;line-height:44px;color:#1d3c6e"><b style="font-weight:600">Get&nbsp; in Touch</b><br><span style="font-weight:400">Contact Us</span></div>
<p class="abs" style="left:140px;top:3386px;width:375px;font-size:12.5px;line-height:21px;color:var(--text)">Lorem ipsum dolor sit amet, consectetur adipiscing e lit, sed do eiusmod tempor incididunt ut labore et dolore magna aliqua. ceptos ...</p>
<div class="abs" style="left:140px;top:3488px;width:378px;height:1px;background:#d4d8de"></div>
<div class="abs c-icon" style="left:139px;top:3519px"></div>
<svg class="abs" style="left:150px;top:3529px" width="14" height="17" viewBox="0 0 8 10"><path d="M4 0a4 4 0 0 1 4 4c0 3-4 6-4 6S0 7 0 4a4 4 0 0 1 4-4z" fill="#3b86c4"/><circle cx="4" cy="4" r="1.4" fill="#fff"/></svg>
<div class="abs c-text" style="left:193px;top:3528px">Elmsgate 7, 3120 Westholm</div>
<div class="abs c-icon" style="left:139px;top:3582px"></div>
<svg class="abs" style="left:149px;top:3592px" width="16" height="16" viewBox="0 0 16 16"><path d="M3 1l3 3-2 2c1 2 3 4 6 6l2-2 3 3-2 2C7 15 1 9 1 3z" fill="#3b86c4"/></svg>
<div class="abs c-text" style="left:193px;top:3591px">+1 209 555 0147</div>
<div class="abs c-icon" style="left:139px;top:3638px"></div>
<svg class="abs" style="left:149px;top:3650px" width="16" height="12" viewBox="0 0 16 12"><rect width="16" height="12" rx="1" fill="#2a3f8f"/><path d="M1 1l7 6 7-6" fill="none" stroke="#fff" stroke-width="1.4"/></svg>
<div class="abs c-text" style="left:193px;top:3647px">office@vep-mail.org</div>

<div class="abs form-card"></div>
<div class="abs label" style="left:624px;top:3270px">Full Name:</div>
<div class="abs field" style="left:619px;top:3302px;width:424px;height:44px">Sed non neque elit.</div>
<div class="abs label" style="left:624px;top:3374px">Email :</div>
<div class="abs label" style="left:851px;top:3374px">Phone no :</div>
<div class="abs field" style="left:619px;top:3405px;width:197px;height:45px">Sed non neque elit.</div>
<div class="abs field" style="left:847px;top:3405px;width:196px;height:45px">Sed non neque elit.</div>
<div class="abs label" style="left:624px;top:3485px">Messages&nbsp; :</div>
<div class="abs field" style="left:619px;top:3515px;width:424px;height:130px;line-height:1;padding-top:16px">Sed non neque elit.</div>
<div class="abs btn-red" style="left:619px;top:3677px;width:126px;height:40px;line-height:40px;font-size:13px">SUBMIT</div>

<!-- footer -->
<svg class="abs" style="left:0;top:3790px" width="1200" height="530" viewBox="0 0 1200 530" aria-hidden="true">
  <path d="M0 230C220 130 520 60 820 45C980 35 1100 30 1200 15V530H0Z" fill="#1b3550"/>
  <path d="M380 100C600 55 900 20 1200 0V42C1000 44 800 60 380 100Z" fill="#9b0d14"/>
  <path d="M380 100C700 50 950 40 1200 42V55C950 55 700 70 380 100Z" fill="#fff" opacity="0"/>
</svg>
<div class="abs f-head" style="left:93px;top:4065px">CONTACT US</div>
<svg class="abs" style="left:93px;top:4110px" width="12" height="15" viewBox="0 0 8 10"><path d="M4 0a4 4 0 0 1 4 4c0 3-4 6-4 6S0 7 0 4a4 4 0 0 1 4-4z" fill="#fff"/><circle cx="4" cy="4" r="1.4" fill="#1b3550"/></svg>
<div class="abs f-text" style="left:126px;top:4104px;width:185px">101- lorem ipsum simple text print type text industry text.</div>
<svg class="abs" style="left:93px;top:4163px" width="14" height="14" viewBox="0 0 16 16"><path d="M3 1l3 3-2 2c1 2 3 4 6 6l2-2 3 3-2 2C7 15 1 9 1 3z" fill="#fff"/></svg>
<div class="abs f-text" style="left:126px;top:4160px">209 555 0182</div>
<svg class="abs" style="left:93px;top:4200px" width="16" height="12" viewBox="0 0 16 12"><rect width="16" height="12" rx="1" fill="#fff"/><path d="M1 1l7 6 7-6" fill="none" stroke="#1b3550" stroke-width="1.4"/></svg>
<div class="abs f-text" style="left:126px;top:4196px">info@vep-mail.org</div>

<div class="abs" style="left:0;width:1200px;text-align:center;top:4010px;font-size:72px;font-weight:700;color:#fff;line-height:1">VEP</div>
<p class="abs f-text" style="left:455px;top:4112px;width:290px;text-align:center">Lorem ipsum dolor sit amet, consectetur adipisc ing elit, sed do eiusmod tempor incididunt bbbbbut bcbbbcbnmx zjzmsmmzm</p>
<div class="abs social" style="left:537px;top:4200px"></div>
<div class="abs social" style="left:582px;top:4200px"></div>
<div class="abs social" style="left:627px;top:4200px"></div>

<div class="abs f-head" style="left:920px;width:186px;text-align:right;top:4065px">OPENING HOURS</div>
<div class="abs f-text" style="left:820px;width:252px;text-align:right;top:4110px">Mon - Fri: 9am - to - 6pm</div>
<div class="abs f-text" style="left:820px;width:252px;text-align:right;top:4140px">Saturday 9am - to - 2pm</div>
<div class="abs f-text" style="left:820px;width:252px;text-align:right;top:4170px">Sunday : <u>Closed</u></div>
<svg class="abs" style="left:1088px;top:4112px" width="16" height="80" viewBox="0 0 16 80" fill="none" stroke="#fff" stroke-width="1.4"><circle cx="8" cy="8" r="6.5"/><path d="M8 4v4h3"/><circle cx="8" cy="38" r="6.5"/><path d="M8 34v4h3"/><circle cx="8" cy="68" r="6.5"/><path d="M8 64v4h3"/></svg>

<div class="abs" style="left:62px;top:4283px;width:1076px;height:1px;background:rgba(255,255,255,.35)"></div>
<div class="abs f-text" style="left:0;width:1200px;text-align:center;top:4293px">VEP</div>

</body>
</html>
```